Dental Medical History Form - Content provided

Design a medical history form for a dental practice. Content is provided so all that is needed is the formatting to make it look great and easy to read.

"Patient Information" to include all information contained in top portion of the "Patient Medical History Form" docx file.

"Medical History" should follow the formatting and content of the "Exact Medical History" file as this is what the entry fields look like in our practice software and so we would like it to match.

1st page - Patient info, allergies, medications, antibiotics, joint replacement, pregnancy.

2nd page - Do you have, or have you had, any of the following? . . . . . . .
Updates

Project Deadline Extended Reason: Picked too short of a deadline to start (2 days) Added Monday, February 13, 2017

Target Market(s)

All ages but must be clear enough for elderly to read. Use as much space as possible to keep font size bigger yet keep to two pages

Industry/Entity Type

Dental

Font styles to use
Sans Serif

Requirements
Must have
• All content provided
• Our logo at the top (file provided)
• Century Gothic Font
• Limit to two pages

```html
<!DOCTYPE html>
<html lang="en">
<head>
<meta charset="utf-8">
<title>Harbour Dental – Confidential Medical History</title>
<link rel="stylesheet" href="https://fonts.googleapis.com/css2?family=Didact+Gothic&family=Montserrat:ital,wght@0,600;0,700;1,700&display=swap">
<style>
:root{
  --sky:#5dcaf2;
  --navy:#0b76ad;
  --grey:#d4d5d7;
  --panel:#efefef;
  --ink:#2b2b2b;
  --soft:#555;
  --box:#5bc5ee;
  --box-line:#1d3b55;
  --backdrop:#808080;
}
*{box-sizing:border-box;margin:0;padding:0}
html,body{width:1200px;height:857px;overflow:hidden}
body{background:var(--backdrop);font-family:"Didact Gothic",sans-serif;color:var(--ink);position:relative}
.page{position:absolute;top:75px;width:493px;height:698px;background:#fff;overflow:hidden}
.page-front{left:109px}
.page-back{left:630px}
.deco{position:absolute;left:0;top:0}
.abs{position:absolute}
.heading{font-family:"Montserrat",sans-serif;font-weight:600;font-size:9.5px;color:var(--ink);white-space:nowrap}
.title{font-family:"Montserrat",sans-serif;font-weight:700;font-size:11.5px;letter-spacing:.2px}
.tag{display:inline-block;background:var(--navy);color:#fff;font-size:8.5px;line-height:11px;padding:0 3px;white-space:nowrap}
.box{display:inline-block;width:13px;height:13px;background:var(--box);border:1px solid var(--box-line);flex:none}
.field{position:absolute;display:flex;align-items:flex-end;height:13px}
.field .rule{flex:1;border-bottom:1px solid #333;margin-left:2px}
.hint{position:absolute;font-size:8px;color:var(--soft);word-spacing:2px;white-space:pre}
.small{font-size:8.5px;color:var(--soft)}
.rule-line{position:absolute;border-bottom:1px solid #333}
.dash{position:absolute;left:8px;width:477px;border-top:1px dashed #a9a9a9}

/* header */
.brand{position:absolute;left:40px;top:10px;font-size:25px;color:#4f6373;letter-spacing:.5px}
.practice{position:absolute;right:12px;top:8px;text-align:right;font-size:11.5px;line-height:13px;color:#333}
.practice .name{font-size:13.5px}

/* front panel */
.panel{position:absolute;left:8px;top:339px;width:477px;height:207px;background:var(--panel)}
.choice-row{position:absolute;display:flex;justify-content:space-between;align-items:center;font-style:italic;color:var(--soft)}
.choice-row span{display:flex;align-items:center;gap:2px;white-space:nowrap}
.allergy{left:12px;width:465px;font-size:9px}
.meds{left:12px;width:465px;font-size:7.8px}
.turnover{position:absolute;left:341px;top:634px;font-family:"Montserrat",sans-serif;font-weight:700;font-style:italic;font-size:14.5px;color:#fff}
.divider{position:absolute;border-left:1px dashed #bbb}

/* back page lists */
.section-tag{position:absolute;font-family:"Montserrat",sans-serif;font-weight:700;font-size:8.5px}
.list{position:absolute}
.item{display:flex;align-items:center;font-size:8.6px;color:#444}
.item .name{flex:1;white-space:nowrap;overflow:hidden}
.item .yes{width:17px;color:var(--soft)}
.item .no{width:15px;margin-left:10px;color:var(--soft)}
.col-left{left:10px;width:228px}
.col-right{left:255px;width:232px}
.signature{position:absolute;top:676px;font-family:"Montserrat",sans-serif;font-weight:700;font-size:11.5px;color:#fff;white-space:nowrap}
.thanks{position:absolute;left:285px;top:667px;width:205px;text-align:center;font-size:5.6px;line-height:7px;color:#fff}
</style>
</head>
<body>

<!-- PAGE ONE -->
<section class="page page-front">
  <svg class="deco" width="493" height="698" viewBox="0 0 493 698" aria-hidden="true">
    <polygon points="287,0 493,0 493,71 371,71" fill="var(--grey)"/>
    <polygon points="0,0 211,0 252,47 0,47" fill="var(--sky)"/>
    <polygon points="211,0 290,0 351,47 252,47" fill="var(--navy)"/>
    <polygon points="136,653 267,653 303,698 180,698" fill="var(--grey)"/>
    <polygon points="0,677 174,677 186,698 0,698" fill="var(--sky)"/>
    <polygon points="246,630 493,630 493,698 303,698" fill="var(--navy)"/>
    <g fill="none" stroke="#fff" stroke-width="4" stroke-linejoin="miter">
      <polyline points="356,661 372,673 356,685"/>
      <polyline points="376,663 390,673 376,683"/>
      <polyline points="394,665 406,673 394,681"/>
      <polyline points="411,667 421,673 411,679"/>
    </g>
  </svg>

  <div class="brand">harbour dental</div>
  <div class="practice">
    <div class="name">Harbour Dental</div>
    <div>3.04/150 Coastal Ridge Rd</div>
    <div>Bayview NSW 2999</div>
    <div>(02) 40 555 018</div>
  </div>

  <div class="abs title" style="left:11px;top:60px">CONFIDENTIAL MEDICAL HISTORY</div>

  <!-- patient details -->
  <div class="field" style="left:11px;top:84px;width:223px"><span class="tag">Name:</span><span class="rule"></span></div>
  <div class="hint" style="left:52px;top:105px">Title   /    First   /   Middle   /    Last</div>
  <div class="field" style="left:11px;top:119px;width:223px"><span class="tag">Address:</span><span class="rule"></span></div>
  <div class="field" style="left:11px;top:136px;width:223px"><span class="tag">DOB:</span><span class="rule"></span></div>
  <div class="field" style="left:11px;top:155px;width:223px"><span class="tag">Email Address:</span><span class="rule"></span></div>
  <div class="field" style="left:11px;top:174px;width:223px"><span class="tag">Phone Number(s):</span><span class="rule"></span></div>
  <div class="hint" style="left:103px;top:190px">Mobile  /   Work  /   Home</div>

  <div class="abs heading" style="left:11px;top:226px">Emergency Contact Person:</div>
  <div class="field" style="left:11px;top:241px;width:223px"><span class="tag">Name:</span><span class="rule"></span></div>
  <div class="field" style="left:11px;top:260px;width:223px"><span class="tag">Relationship:</span><span class="rule"></span></div>
  <div class="field" style="left:11px;top:279px;width:223px"><span class="tag">Phone Number:</span><span class="rule"></span></div>

  <div class="divider" style="left:245px;top:61px;height:276px"></div>

  <!-- practitioner & fund -->
  <div class="abs heading" style="left:257px;top:80px">General Practitioner:</div>
  <div class="field" style="left:257px;top:95px;width:224px"><span class="tag">Name:</span><span class="rule"></span></div>
  <div class="field" style="left:257px;top:115px;width:224px"><span class="tag">Practice Name:</span><span class="rule"></span></div>
  <div class="field" style="left:257px;top:132px;width:224px"><span class="tag">Phone Number:</span><span class="rule"></span></div>
  <div class="abs heading" style="left:257px;top:155px">Do you have a health fund with dental cover?</div>
  <span class="abs small" style="left:289px;top:173px">Yes</span><span class="abs box" style="left:310px;top:171px"></span>
  <span class="abs small" style="left:377px;top:173px">No</span><span class="abs box" style="left:397px;top:171px"></span>
  <div class="abs heading" style="left:257px;top:193px">If so, what is the name of the fund?</div>
  <div class="rule-line" style="left:257px;top:216px;width:224px"></div>
  <div class="abs heading" style="left:257px;top:221px">Fund Number?</div>
  <div class="rule-line" style="left:257px;top:244px;width:224px"></div>
  <div class="abs heading" style="left:257px;top:249px">Priority Number on card:</div>
  <span class="abs heading" style="left:265px;top:267px">1</span><span class="abs box" style="left:276px;top:265px"></span>
  <span class="abs heading" style="left:308px;top:267px">2</span><span class="abs box" style="left:321px;top:265px"></span>
  <span class="abs heading" style="left:353px;top:267px">3</span><span class="abs box" style="left:365px;top:265px"></span>
  <span class="abs heading" style="left:394px;top:267px">4</span><span class="abs box" style="left:404px;top:265px"></span>
  <span class="abs heading" style="left:434px;top:267px">5</span><span class="abs box" style="left:445px;top:265px"></span>
  <div class="field" style="left:257px;top:288px;width:224px"><span class="tag">Occupation:</span><span class="rule"></span></div>
  <div class="field" style="left:257px;top:307px;width:224px"><span class="tag">Referred by:</span><span class="rule"></span></div>

  <!-- allergies & medication -->
  <div class="panel"></div>
  <div class="abs heading" style="left:11px;top:342px">Please indicate if  you are allergic to any of the following?</div>
  <div class="choice-row allergy" style="top:356px">
    <span>Aspirin<i class="box"></i></span><span>Codeine<i class="box"></i></span><span>Penicillin<i class="box"></i></span><span>Sulfites<i class="box"></i></span><span>Latex<i class="box"></i></span><span>Local Anaesthetic<i class="box"></i></span><span>Lactose<i class="box"></i></span><span>Nickel<i class="box"></i></span>
  </div>
  <div class="abs heading" style="left:11px;top:380px;font-weight:600">Other:</div>
  <div class="rule-line" style="left:44px;top:391px;width:425px"></div>
  <div class="dash" style="top:396px"></div>
  <div class="abs heading" style="left:11px;top:400px">Are you currently taking, or have ever taken, any of the following medication?</div>
  <div class="choice-row meds" style="top:414px">
    <span>Asthma inhaler<i class="box"></i></span><span>Anti-epileptics<i class="box"></i></span><span>Anti-depressants<i class="box"></i></span><span>Blood Pressure<i class="box"></i></span><span>Blood Thinners<i class="box"></i></span><span>Bisphosphonates<i class="box"></i></span>
  </div>
  <div class="choice-row meds" style="top:433px">
    <span>Chemotherapy<i class="box"></i></span><span>Insulin<i class="box"></i></span><span>Immunosuppressants<i class="box"></i></span><span>Steroids<i class="box"></i></span><span>Oral Contraceptive<i class="box"></i></span><span>Other<i class="box"></i></span>
  </div>
  <div class="dash" style="top:461px"></div>
  <div class="abs heading" style="left:11px;top:467px">Please specify medication name, dose, and frequency where possible:</div>
  <div class="rule-line" style="left:11px;top:493px;width:470px"></div>
  <div class="rule-line" style="left:11px;top:514px;width:470px"></div>
  <div class="rule-line" style="left:11px;top:536px;width:470px"></div>
  <div class="dash" style="top:546px"></div>

  <!-- other questions -->
  <div class="abs heading" style="left:11px;top:553px">Do you require antibiotic cover?</div>
  <span class="abs small" style="left:189px;top:554px;font-style:italic">Yes</span><span class="abs box" style="left:207px;top:552px"></span>
  <span class="abs small" style="left:243px;top:554px">No</span><span class="abs box" style="left:259px;top:552px"></span>
  <div class="abs heading" style="left:11px;top:576px">Have you had a joint replacement?</div>
  <span class="abs small" style="left:189px;top:577px;font-style:italic">Yes</span><span class="abs box" style="left:207px;top:575px"></span>
  <span class="abs small" style="left:243px;top:577px">No</span><span class="abs box" style="left:259px;top:575px"></span>
  <span class="abs tag" style="left:11px;top:596px">Women:</span>
  <div class="abs heading" style="left:11px;top:610px">Are you pregnant?</div>
  <span class="abs small" style="left:110px;top:611px">Yes</span><span class="abs box" style="left:129px;top:609px"></span>
  <span class="abs small" style="left:166px;top:611px">No</span><span class="abs box" style="left:181px;top:609px"></span>
  <span class="abs small" style="left:217px;top:611px">or</span>
  <div class="abs heading" style="left:246px;top:610px">Breast Feeding?</div>
  <span class="abs small" style="left:335px;top:611px">Yes</span><span class="abs box" style="left:354px;top:609px"></span>
  <span class="abs small" style="left:390px;top:611px">No</span><span class="abs box" style="left:405px;top:609px"></span>

  <div class="turnover">Please Turnover</div>
</section>

<!-- PAGE TWO -->
<section class="page page-back">
  <svg class="deco" width="493" height="698" viewBox="0 0 493 698" aria-hidden="true">
    <polygon points="0,0 360,0 372,10 0,10" fill="var(--sky)"/>
    <polygon points="300,0 493,0 493,35 300,35" fill="var(--grey)"/>
    <polygon points="300,0 350,0 373,10 316,10" fill="var(--navy)"/>
    <polygon points="0,655 162,655 194,698 0,698" fill="var(--navy)"/>
    <polygon points="154,668 262,668 282,698 176,698" fill="var(--grey)"/>
    <polygon points="265,662 493,662 493,698 282,698" fill="var(--sky)"/>
  </svg>

  <div class="abs title" style="left:10px;top:20px;font-weight:600">Do you have, or have you had, any of the following?</div>
  <div class="divider" style="left:245px;top:37px;height:632px"></div>

  <!-- left column -->
  <span class="section-tag tag" style="left:10px;top:44px">Dental</span>
  <div class="list col-left" style="top:53.4px">
    <div class="item" style="height:16.4px"><span class="name">Acid Reflux</span><span class="yes">Yes</span><i class="box"></i><span class="no">No</span><i class="box"></i></div>
    <div class="item" style="height:16.4px"><span class="name">Bad Breath/Taste</span><span class="yes">Yes</span><i class="box"></i><span class="no">No</span><i class="box"></i></div>
    <div class="item" style="height:16.4px"><span class="name">Bleeding/Swollen/Sore Gums</span><span class="yes">Yes</span><i class="box"></i><span class="no">No</span><i class="box"></i></div>
    <div class="item" style="height:16.4px"><span class="name">Blisters/Ulcers in Mouth</span><span class="yes">Yes</span><i class="box"></i><span class="no">No</span><i class="box"></i></div>
    <div class="item" style="height:16.4px"><span class="name">Broken tooth/filling</span><span class="yes">Yes</span><i class="box"></i><span class="no">No</span><i class="box"></i></div>
    <div class="item" style="height:16.4px"><span class="name">Burning tongue</span><span class="yes">Yes</span><i class="box"></i><span class="no">No</span><i class="box"></i></div>
    <div class="item" style="height:16.4px"><span class="name">Dry mouth</span><span class="yes">Yes</span><i class="box"></i><span class="no">No</span><i class="box"></i></div>
    <div class="item" style="height:16.4px"><span class="name">Food collection between teeth</span><span class="yes">Yes</span><i class="box"></i><span class="no">No</span><i class="box"></i></div>
    <div class="item" style="height:16.4px"><span class="name">Grinding/clenching teeth (day/night)</span><span class="yes">Yes</span><i class="box"></i><span class="no">No</span><i class="box"></i></div>
    <div class="item" style="height:16.4px"><span class="name">Loose teeth</span><span class="yes">Yes</span><i class="box"></i><span class="no">No</span><i class="box"></i></div>
    <div class="item" style="height:16.4px"><span class="name">Crooked teeth</span><span class="yes">Yes</span><i class="box"></i><span class="no">No</span><i class="box"></i></div>
    <div class="item" style="height:16.4px"><span class="name">Discoloured teeth</span><span class="yes">Yes</span><i class="box"></i><span class="no">No</span><i class="box"></i></div>
    <div class="item" style="height:16.4px"><span class="name">Sensitivity to Hot/Cold</span><span class="yes">Yes</span><i class="box"></i><span class="no">No</span><i class="box"></i></div>
    <div class="item" style="height:16.4px"><span class="name">Tooth pain when chewing</span><span class="yes">Yes</span><i class="box"></i><span class="no">No</span><i class="box"></i></div>
    <div class="item" style="height:16.4px"><span class="name">Jaw pain/Fracture</span><span class="yes">Yes</span><i class="box"></i><span class="no">No</span><i class="box"></i></div>
    <div class="item" style="height:16.4px"><span class="name">Orthodontic treatment/history</span><span class="yes">Yes</span><i class="box"></i><span class="no">No</span><i class="box"></i></div>
    <div class="item" style="height:16.4px"><span class="name">Oral Cancer</span><span class="yes">Yes</span><i class="box"></i><span class="no">No</span><i class="box"></i></div>
  </div>

  <span class="section-tag tag" style="left:10px;top:336px">Diet/Lifestyle</span>
  <div class="list col-left" style="top:346.6px">
    <div class="item" style="height:16.8px"><span class="name" style="font-size:7.4px">Drink more than one glass alcohol per day</span><span class="yes">Yes</span><i class="box"></i><span class="no">No</span><i class="box"></i></div>
    <div class="item" style="height:16.8px"><span class="name">Smoking</span><span class="yes">Yes</span><i class="box"></i><span class="no">No</span><i class="box"></i></div>
    <div class="item" style="height:16.8px"><span class="name">Carbonated drinks</span><span class="yes">Yes</span><i class="box"></i><span class="no">No</span><i class="box"></i></div>
    <div class="item" style="height:16.8px"><span class="name">Sugary foods</span><span class="yes">Yes</span><i class="box"></i><span class="no">No</span><i class="box"></i></div>
  </div>

  <span class="section-tag tag" style="left:10px;top:417px">Blood</span>
  <div class="list col-left" style="top:427.7px">
    <div class="item" style="height:16.6px"><span class="name">Anaemia</span><span class="yes">Yes</span><i class="box"></i><span class="no">No</span><i class="box"></i></div>
    <div class="item" style="height:16.6px"><span class="name">Blood clots</span><span class="yes">Yes</span><i class="box"></i><span class="no">No</span><i class="box"></i></div>
    <div class="item" style="height:16.6px"><span class="name">Leukemia</span><span class="yes">Yes</span><i class="box"></i><span class="no">No</span><i class="box"></i></div>
    <div class="item" style="height:16.6px"><span class="name">Low platelets</span><span class="yes">Yes</span><i class="box"></i><span class="no">No</span><i class="box"></i></div>
    <div class="item" style="height:16.6px"><span class="name">Lymphoma</span><span class="yes">Yes</span><i class="box"></i><span class="no">No</span><i class="box"></i></div>
    <div class="item" style="height:16.6px"><span class="name">Haemophelia</span><span class="yes">Yes</span><i class="box"></i><span class="no">No</span><i class="box"></i></div>
  </div>

  <span class="section-tag tag" style="left:10px;top:530px">Chest</span>
  <div class="list col-left" style="top:539.6px">
    <div class="item" style="height:16.8px"><span class="name">Bronchitis</span><span class="yes">Yes</span><i class="box"></i><span class="no">No</span><i class="box"></i></div>
    <div class="item" style="height:16.8px"><span class="name">Cystic Fibrosis</span><span class="yes">Yes</span><i class="box"></i><span class="no">No</span><i class="box"></i></div>
    <div class="item" style="height:16.8px"><span class="name">Emphysema</span><span class="yes">Yes</span><i class="box"></i><span class="no">No</span><i class="box"></i></div>
    <div class="item" style="height:16.8px"><span class="name">Pneumonia</span><span class="yes">Yes</span><i class="box"></i><span class="no">No</span><i class="box"></i></div>
  </div>

  <span class="section-tag tag" style="left:10px;top:609px">Other</span>
  <div class="rule-line" style="left:10px;top:629px;width:228px"></div>
  <div class="rule-line" style="left:10px;top:646px;width:228px"></div>

  <!-- right column -->
  <span class="section-tag tag" style="left:255px;top:37px">Infectious Disease</span>
  <div class="list col-right" style="top:46.9px">
    <div class="item" style="height:16.2px"><span class="name">Creutzfeldt-Jakob Disease</span><span class="yes">Yes</span><i class="box"></i><span class="no">No</span><i class="box"></i></div>
    <div class="item" style="height:16.2px"><span class="name">Hepatitis A,B,C,D</span><span class="yes">Yes</span><i class="box"></i><span class="no">No</span><i class="box"></i></div>
    <div class="item" style="height:16.2px"><span class="name">HIV/AIDS</span><span class="yes">Yes</span><i class="box"></i><span class="no">No</span><i class="box"></i></div>
    <div class="item" style="height:16.2px"><span class="name">Influenza</span><span class="yes">Yes</span><i class="box"></i><span class="no">No</span><i class="box"></i></div>
    <div class="item" style="height:16.2px"><span class="name">Shingles</span><span class="yes">Yes</span><i class="box"></i><span class="no">No</span><i class="box"></i></div>
    <div class="item" style="height:16.2px"><span class="name">Tuberculosis</span><span class="yes">Yes</span><i class="box"></i><span class="no">No</span><i class="box"></i></div>
  </div>

  <span class="section-tag tag" style="left:255px;top:143px">Heart</span>
  <div class="list col-right" style="top:152.8px">
    <div class="item" style="height:16.4px"><span class="name">Angina</span><span class="yes">Yes</span><i class="box"></i><span class="no">No</span><i class="box"></i></div>
    <div class="item" style="height:16.4px"><span class="name">Atrial Fibrillation</span><span class="yes">Yes</span><i class="box"></i><span class="no">No</span><i class="box"></i></div>
    <div class="item" style="height:16.4px"><span class="name">Blood Pressure (High/Low)</span><span class="yes">Yes</span><i class="box"></i><span class="no">No</span><i class="box"></i></div>
    <div class="item" style="height:16.4px"><span class="name">Congenital Heart Disease</span><span class="yes">Yes</span><i class="box"></i><span class="no">No</span><i class="box"></i></div>
    <div class="item" style="height:16.4px"><span class="name">Heart attack</span><span class="yes">Yes</span><i class="box"></i><span class="no">No</span><i class="box"></i></div>
    <div class="item" style="height:16.4px"><span class="name">Heart murmur</span><span class="yes">Yes</span><i class="box"></i><span class="no">No</span><i class="box"></i></div>
    <div class="item" style="height:16.4px"><span class="name">Heart surgery</span><span class="yes">Yes</span><i class="box"></i><span class="no">No</span><i class="box"></i></div>
    <div class="item" style="height:16.4px"><span class="name">Heart valve replacement</span><span class="yes">Yes</span><i class="box"></i><span class="no">No</span><i class="box"></i></div>
    <div class="item" style="height:16.4px"><span class="name">Infective endocarditis</span><span class="yes">Yes</span><i class="box"></i><span class="no">No</span><i class="box"></i></div>
    <div class="item" style="height:16.4px"><span class="name">Rheumatic Heart Disease</span><span class="yes">Yes</span><i class="box"></i><span class="no">No</span><i class="box"></i></div>
    <div class="item" style="height:16.4px"><span class="name">Pacemaker</span><span class="yes">Yes</span><i class="box"></i><span class="no">No</span><i class="box"></i></div>
    <div class="item" style="height:16.4px"><span class="name">Stent</span><span class="yes">Yes</span><i class="box"></i><span class="no">No</span><i class="box"></i></div>
  </div>

  <span class="section-tag tag" style="left:255px;top:348px">Other</span>
  <div class="list col-right" style="top:357.6px">
    <div class="item" style="height:16.9px"><span class="name">Anxiety/PTSD</span><span class="yes">Yes</span><i class="box"></i><span class="no">No</span><i class="box"></i></div>
    <div class="item" style="height:16.9px"><span class="name">Arthritis</span><span class="yes">Yes</span><i class="box"></i><span class="no">No</span><i class="box"></i></div>
    <div class="item" style="height:16.9px"><span class="name">Alzheimer’s</span><span class="yes">Yes</span><i class="box"></i><span class="no">No</span><i class="box"></i></div>
    <div class="item" style="height:16.9px"><span class="name">Asthma</span><span class="yes">Yes</span><i class="box"></i><span class="no">No</span><i class="box"></i></div>
    <div class="item" style="height:16.9px"><span class="name">Anaphylaxis</span><span class="yes">Yes</span><i class="box"></i><span class="no">No</span><i class="box"></i></div>
    <div class="item" style="height:16.9px"><span class="name">Auto-immune disease</span><span class="yes">Yes</span><i class="box"></i><span class="no">No</span><i class="box"></i></div>
    <div class="item" style="height:16.9px"><span class="name">Coeliac</span><span class="yes">Yes</span><i class="box"></i><span class="no">No</span><i class="box"></i></div>
    <div class="item" style="height:16.9px"><span class="name">Diabetes</span><span class="yes">Yes</span><i class="box"></i><span class="no">No</span><i class="box"></i></div>
    <div class="item" style="height:16.9px"><span class="name">Epilepsy</span><span class="yes">Yes</span><i class="box"></i><span class="no">No</span><i class="box"></i></div>
    <div class="item" style="height:16.9px"><span class="name">Kidney Disease</span><span class="yes">Yes</span><i class="box"></i><span class="no">No</span><i class="box"></i></div>
    <div class="item" style="height:16.9px"><span class="name">Liver Disease</span><span class="yes">Yes</span><i class="box"></i><span class="no">No</span><i class="box"></i></div>
    <div class="item" style="height:16.9px"><span class="name">Osteoporosis</span><span class="yes">Yes</span><i class="box"></i><span class="no">No</span><i class="box"></i></div>
    <div class="item" style="height:16.9px"><span class="name">Parkinson’s</span><span class="yes">Yes</span><i class="box"></i><span class="no">No</span><i class="box"></i></div>
    <div class="item" style="height:16.9px"><span class="name">Radiation to Head/Neck</span><span class="yes">Yes</span><i class="box"></i><span class="no">No</span><i class="box"></i></div>
    <div class="item" style="height:16.9px"><span class="name">Schizophrenia</span><span class="yes">Yes</span><i class="box"></i><span class="no">No</span><i class="box"></i></div>
    <div class="item" style="height:16.9px"><span class="name">Snoring</span><span class="yes">Yes</span><i class="box"></i><span class="no">No</span><i class="box"></i></div>
    <div class="item" style="height:16.9px"><span class="name">Sleep apnea</span><span class="yes">Yes</span><i class="box"></i><span class="no">No</span><i class="box"></i></div>
    <div class="item" style="height:16.9px"><span class="name">Stroke</span><span class="yes">Yes</span><i class="box"></i><span class="no">No</span><i class="box"></i></div>
  </div>

  <div class="signature" style="left:6px">Signature:<span style="display:inline-block;width:105px;border-bottom:1px solid #fff"></span></div>
  <div class="signature" style="left:179px">Date:<span style="display:inline-block;width:72px;border-bottom:1px solid #fff"></span></div>
  <p class="thanks">Thank you for the time to complete your medical history form.<br>Oral health is linked to overall health and this comprehensive<br>questionnaire will help us to provide you with optimal and safe care.</p>
</section>

</body>
</html>
```